Brindale transport business cards

Front of card, Looking for my logo on one side of the card

Back of card,
Brindale Transport Maintenance
Onsite Cars, Trucks & trailer maintenance and repairs
Ronan Brindale
0452819036
Brindaletm@fernmail.com

```html
<!DOCTYPE html>
<html lang="en">
<head>
<meta charset="utf-8">
<title>Brindale Transport Maintenance – Business Cards</title>
<link href="https://fonts.googleapis.com/css2?family=Alfa+Slab+One&family=Oswald:wght@400;500;600&family=Russo+One&display=swap" rel="stylesheet">
<style>
  :root {
    --stage: #1e1e1e;
    --ink: #000000;
    --paper: #ffffff;
    --blue: #0a84e0;
    --blue-deep: #143a78;
    --silver: #a59a9a;
    --silver-light: #d8d2d2;
    --grey-text: #8c7f7f;
  }
  * { margin: 0; padding: 0; box-sizing: border-box; }
  html, body { width: 1200px; height: 1015px; overflow: hidden; }
  body {
    background: radial-gradient(ellipse at center, #2c2c2c 0%, var(--stage) 60%, #0e0e0e 100%);
    position: relative;
    font-family: "Oswald", "Arial Narrow", sans-serif;
  }
  .card {
    position: absolute;
    width: 600px;
    height: 343px;
    overflow: hidden;
    box-shadow: 0 18px 40px rgba(0,0,0,.6);
  }
  .card--front { left: 70px; top: 100px; background: var(--ink); }
  .card--back { left: 530px; top: 570px; background: var(--paper); }
  .card__shapes { position: absolute; inset: 0; }

  /* front */
  .brand {
    position: absolute; left: 150px; top: 52px;
    display: flex; align-items: center; gap: 14px;
    color: var(--paper);
  }
  .brand__mark { width: 34px; height: 34px; background: var(--blue); flex: none; }
  .brand__name { font-family: "Alfa Slab One", Georgia, serif; font-size: 44px; line-height: 1; letter-spacing: 1px; }
  .brand__sub { display: block; font-family: "Oswald", "Arial Narrow", sans-serif; font-weight: 400; font-size: 16px; letter-spacing: 1.5px; margin-top: 6px; }
  .front__phone {
    position: absolute; left: 0; right: 0; top: 140px; text-align: center;
    font-family: "Russo One", sans-serif; font-size: 66px; letter-spacing: 4px;
    color: var(--paper);
  }
  .front__tagline {
    position: absolute; left: 0; right: 0; top: 262px; text-align: center;
    font-weight: 600; font-size: 21px; letter-spacing: .2px;
    color: var(--paper); text-transform: uppercase;
  }

  /* back */
  .person {
    position: absolute; left: 42px; top: 46px;
    font-family: "Alfa Slab One", Georgia, serif; font-size: 30px; font-weight: 400;
    color: var(--blue); letter-spacing: 1px; text-transform: uppercase; line-height: 1.1;
  }
  .person__rule { position: absolute; left: 42px; top: 98px; width: 90px; height: 4px; background: var(--paper); }
  .contact { position: absolute; left: 42px; list-style: none; color: var(--paper); font-weight: 500; font-size: 20px; letter-spacing: .3px; }
  .contact li { display: flex; align-items: center; gap: 14px; height: 38px; }
  .contact svg { width: 28px; height: 28px; flex: none; }
  .contact--list { top: 112px; }
  .contact__mail { text-transform: uppercase; }
  .back__brand {
    position: absolute; left: 60px; top: 232px;
  }
  .back__brand-name { font-family: "Alfa Slab One", Georgia, serif; color: var(--ink); font-size: 36px; line-height: 1; letter-spacing: 1px; }
  .back__brand-sub { font-family: "Oswald", "Arial Narrow", sans-serif; font-weight: 500; color: var(--grey-text); font-size: 15px; line-height: 1.2; letter-spacing: 1px; margin-top: 3px; }
  .truck-art {
    position: absolute; left: 420px; top: 60px; width: 180px; height: 190px;
    background: linear-gradient(160deg, var(--blue) 0%, var(--blue-deep) 100%);
  }
</style>
</head>
<body>

<section class="card card--front" aria-label="Business card front">
  <svg class="card__shapes" viewBox="0 0 600 343" aria-hidden="true">
    <defs>
      <linearGradient id="bandBlue" x1="0" x2="1">
        <stop offset="0" stop-color="#0a84e0"/>
        <stop offset="1" stop-color="#143a78"/>
      </linearGradient>
      <linearGradient id="silverFade" x1="0" x2="1">
        <stop offset="0" stop-color="#d8d2d2"/>
        <stop offset="1" stop-color="#8c7f7f"/>
      </linearGradient>
    </defs>
    <rect x="0" y="246" width="600" height="4" fill="url(#silverFade)"/>
    <rect x="0" y="250" width="600" height="62" fill="url(#bandBlue)"/>
    <rect x="330" y="240" width="270" height="6" fill="#8c7f7f"/>
    <rect x="0" y="312" width="600" height="4" fill="#5a5050"/>
  </svg>
  <div class="brand">
    <span class="brand__mark"></span>
    <div>
      <div class="brand__name">BRINDALE</div>
      <span class="brand__sub">TRANSPORT MAINTENANCE</span>
    </div>
  </div>
  <div class="front__phone">0452819036</div>
  <p class="front__tagline">Onsite Cars, Trucks &amp; Trailer Maintenance and Repairs</p>
</section>

<section class="card card--back" aria-label="Business card back">
  <svg class="card__shapes" viewBox="0 0 600 343" aria-hidden="true">
    <defs>
      <linearGradient id="stripeBlue" x1="0" x2="1">
        <stop offset="0" stop-color="#0a84e0"/>
        <stop offset="1" stop-color="#143a78"/>
      </linearGradient>
    </defs>
    <polygon points="0,0 405,0 352,198 0,222" fill="#000"/>
    <polygon points="0,296 345,296 358,272 366,272 350,308 0,308" fill="url(#stripeBlue)"/>
    <polygon points="0,314 354,314 388,250 600,250 600,343 0,343" fill="#000"/>
    <rect x="560" y="214" width="40" height="16" fill="#a59a9a"/>
  </svg>
  <div class="truck-art" role="img" aria-label="Illustration of a blue truck cab with chrome exhaust stack"></div>

  <h1 class="person">Ronan Brindale</h1>
  <div class="person__rule"></div>
  <ul class="contact contact--list">
    <li>
      <svg viewBox="0 0 28 28" aria-hidden="true"><circle cx="14" cy="14" r="14" fill="var(--blue)"/><path d="M10 8c1 0 2 3 2 3l-1.5 1.5c.8 2 2.2 3.4 4 4l1.5-1.5s3 1 3 2-1.5 2.5-3 2.5C11 19.5 8.5 13 8.5 10.5 8.5 9 9 8 10 8z" fill="#fff"/></svg>
      <span>0452819036</span>
    </li>
    <li>
      <svg viewBox="0 0 28 28" aria-hidden="true"><circle cx="14" cy="14" r="14" fill="var(--blue)"/><rect x="7" y="9" width="14" height="10" fill="#fff"/><path d="M7 9l7 6 7-6" fill="none" stroke="var(--blue)" stroke-width="1.4"/></svg>
      <span class="contact__mail">Brindaletm@fernmail.com</span>
    </li>
  </ul>
  <div class="back__brand">
    <div class="back__brand-name">BRINDALE</div>
    <div class="back__brand-sub">TRANSPORT MAINTENANCE</div>
  </div>
</section>

</body>
</html>
```